Business Cards, Letterheads, Envelopes

A company's new identity to be reflected on its stationery items

Target Market(s)

Large Corporate Companies & Enterprises

Font styles to use
Sans Serif

Colors
0555a3
3176b5
85abd2
85cae6
33a6d7
0293ce

```html
<!DOCTYPE html>
<html lang="en">
<head>
<meta charset="utf-8">
<title>Corvalis Nexa Stationery</title>
<link rel="stylesheet" href="https://fonts.googleapis.com/css2?family=Orbitron:wght@500;700&family=Questrial&family=Saira+Condensed:wght@300&display=swap">
<style>
  :root {
    --navy: #033d66;
    --blue: #3176b5;
    --blue-bright: #0293ce;
    --blue-soft: #85abd2;
    --rule: #9a9a9a;
    --ink: #1d3550;
    --paper: #ffffff;
    --backdrop: #dcdfe3;
  }
  * { margin: 0; padding: 0; box-sizing: border-box; }
  html, body { width: 1200px; height: 952px; overflow: hidden; }
  body { position: relative; background: var(--backdrop); font-family: "Questrial", sans-serif; color: var(--ink); }
  .sheet { position: absolute; background: var(--paper); box-shadow: 0 2px 6px rgba(0,0,0,.25); overflow: hidden; }
  .abs { position: absolute; white-space: nowrap; }
  .brand-mark { position: absolute; border-radius: 50%; background: var(--blue); }
  .brand-name { font-family: "Orbitron", sans-serif; font-weight: 700; color: var(--blue); line-height: 1; }
  .brand-sub { font-family: "Orbitron", sans-serif; font-weight: 700; color: var(--blue); letter-spacing: .16em; line-height: 1; }
  .tagline { font-family: "Orbitron", sans-serif; font-weight: 500; color: var(--rule); letter-spacing: .3em; line-height: 1; }
  .header-rule { position: absolute; height: 1px; background: var(--rule); }
  .country { font-family: "Orbitron", sans-serif; font-weight: 500; color: var(--blue); line-height: 1; letter-spacing: .05em; }
  .address { font-size: 8px; line-height: 11px; letter-spacing: .04em; }
  .footer-band { position: absolute; left: 0; right: 0; bottom: 0; background: var(--navy); color: #fff; font-size: 9.5px; letter-spacing: .18em; }
  .footer-band span { position: absolute; top: 50%; transform: translate(-50%, -50%); }
  .footer-sep { position: absolute; top: 3px; bottom: 3px; width: 1px; background: #fff; opacity: .8; }

  /* letterhead */
  .letterhead { left: 28px; top: 37px; width: 565px; height: 842px; }
  .letterhead .footer-band { height: 16px; }

  /* envelope */
  .envelope { left: 611px; top: 37px; width: 575px; height: 288px; }
  .envelope .footer-band { height: 21px; font-size: 10px; }

  /* business cards */
  .card { border-radius: 14px; }
  .card-front { left: 697px; top: 343px; width: 402px; height: 229px; background: var(--navy); color: #fff; text-align: center; }
  .card-front .brand-name, .card-front .brand-sub { color: #fff; }
  .card-back { left: 697px; top: 622px; width: 402px; height: 228px; }
  .card-strip { position: absolute; left: 0; top: 0; bottom: 0; width: 18px; background: var(--navy); }
  .strip-web { position: absolute; left: 9px; top: 50%; transform: translate(-50%, -50%) rotate(-90deg); color: #fff; font-size: 10px; letter-spacing: .2em; white-space: nowrap; }
  .holder-name { font-family: "Orbitron", sans-serif; font-weight: 500; color: var(--blue); font-size: 25px; letter-spacing: .22em; line-height: 1; }
  .holder-phone { font-family: "Saira Condensed", sans-serif; font-weight: 300; color: var(--navy); font-size: 19px; letter-spacing: .18em; line-height: 1; }
  .fade-rule { position: absolute; height: 1px; background: linear-gradient(90deg, transparent, var(--blue-soft), transparent); }
  .card-tag { font-family: "Orbitron", sans-serif; font-weight: 500; letter-spacing: .35em; font-size: 9px; line-height: 1; }
</style>
</head>
<body>

<!-- Letterhead -->
<section class="sheet letterhead" aria-label="Letterhead">
  <div class="brand-mark" style="left:26px;top:20px;width:26px;height:26px;"></div>
  <div class="abs brand-name" style="left:75px;top:30px;font-size:11.5px;">CORVALIS NEXA</div>
  <div class="abs brand-sub" style="left:75px;top:43px;font-size:7.5px;">PRIVATE LIMITED</div>
  <div class="header-rule" style="left:75px;top:51px;width:423px;"></div>
  <div class="abs tagline" style="left:75px;top:55px;font-size:5.5px;">POWERED BY INNOVATION</div>

  <div class="abs country" style="left:10px;top:785px;font-size:12px;">INDIA</div>
  <div class="abs address" style="left:10px;top:798px;">#114-B, Lakeview Industrial Road, Nandipur, Karnataka 570099, IN<br>Phone : 0821-5550192</div>

  <div class="footer-band">
    <span style="left:121px;">hello@corvalisnexa.com</span>
    <div class="footer-sep" style="left:280px;"></div>
    <span style="left:436px;">www.corvalisnexa.com</span>
  </div>
</section>

<!-- Envelope -->
<section class="sheet envelope" aria-label="Envelope">
  <div class="brand-mark" style="left:15px;top:12px;width:24px;height:24px;"></div>
  <div class="abs brand-name" style="left:61px;top:17px;font-size:11px;">CORVALIS NEXA</div>
  <div class="abs brand-sub" style="left:61px;top:28px;font-size:7px;">PRIVATE LIMITED</div>
  <div class="header-rule" style="left:61px;top:36px;width:432px;"></div>
  <div class="abs tagline" style="left:61px;top:39px;font-size:5px;">POWERED BY INNOVATION</div>

  <div class="abs country" style="left:9px;top:233px;font-size:12px;">INDIA</div>
  <div class="abs address" style="left:9px;top:247px;">#114-B, Lakeview Industrial Road, Nandipur, Karnataka 570099, IN<br>phone : 0821-5550192</div>

  <div class="footer-band">
    <span style="left:105px;">hello@corvalisnexa.com</span>
    <div class="footer-sep" style="left:286px;"></div>
    <span style="left:469px;">www.corvalisnexa.com</span>
  </div>
</section>

<!-- Business card, front -->
<section class="sheet card card-front" aria-label="Business card front">
  <div class="brand-mark" style="left:166px;top:32px;width:70px;height:70px;background:#fff;"></div>
  <div class="abs brand-name" style="left:0;right:0;top:161px;font-size:17px;">CORVALIS NEXA</div>
  <div class="abs brand-sub" style="left:0;right:0;top:179px;font-size:10px;letter-spacing:.28em;">PRIVATE LIMITED</div>
  <div class="fade-rule" style="left:56px;right:56px;top:196px;"></div>
  <div class="abs card-tag" style="left:0;right:0;top:204px;color:var(--blue-bright);">POWERED BY INNOVATION</div>
</section>

<!-- Business card, back -->
<section class="sheet card card-back" aria-label="Business card back">
  <div class="card-strip"><div class="strip-web">www.corvalisnexa.com</div></div>
  <div class="abs holder-name" style="left:36px;top:16px;">FULL NAME</div>
  <div class="abs holder-phone" style="left:36px;top:42px;">0821-5550192</div>
  <div class="brand-mark" style="left:298px;top:24px;width:60px;height:60px;"></div>

  <div class="abs brand-name" style="left:18px;right:0;top:122px;font-size:12.5px;text-align:center;">CORVALIS NEXA</div>
  <div class="abs brand-sub" style="left:18px;right:0;top:136px;font-size:8px;text-align:center;letter-spacing:.25em;">PRIVATE LIMITED</div>
  <div class="fade-rule" style="left:85px;right:100px;top:150px;"></div>
  <div class="abs card-tag" style="left:18px;right:0;top:158px;text-align:center;color:var(--blue-bright);">POWERED BY INNOVATION</div>

  <div class="abs country" style="left:28px;top:181px;font-size:15px;">INDIA</div>
  <div class="abs" style="left:28px;top:200px;font-size:9.5px;letter-spacing:.04em;">#114-B, Lakeview Industrial Road, Nandipur, Karnataka 570099, IN</div>
  <div class="abs" style="left:52px;top:214px;font-size:9.5px;letter-spacing:.04em;">Phone : 0821-5550192</div>
  <div class="abs" style="left:219px;top:214px;font-size:9.5px;letter-spacing:.04em;">hello@corvalisnexa.com</div>
</section>

</body>
</html>
```